Prom Night 2011 theme

I am looking for a theme to best represent a high school "prom night". Design will be printed on slightly smaller than business card size paper. This is a clean sheet design, nothing is out of bounds so use you imagination. Target audience is high school age students. Design should have text "Prom Night 2011" incorporated into it. Colors are limitless.

```html
<!DOCTYPE html>
<html lang="en">
<head>
<meta charset="utf-8">
<title>Prom Night 2011</title>
<link rel="stylesheet" href="https://fonts.googleapis.com/css2?family=Roboto:wght@100;300&display=swap">
<style>
  :root {
    --stage: #4f5457;
    --card-light: #3b86d6;
    --card-mid: #2d2a9e;
    --card-deep: #1a0f5c;
    --card-dark: #0a0620;
    --band: #000000;
    --title: #ffffff;
    --verse: #c9cdf5;
    --glow-cyan: rgba(90, 230, 255, 0.55);
    --glow-violet: rgba(170, 80, 230, 0.45);
  }
  html, body {
    margin: 0;
    width: 1200px;
    height: 927px;
    overflow: hidden;
    background: var(--stage);
  }
  .canvas {
    position: relative;
    width: 1200px;
    height: 927px;
  }
  .ticket {
    position: absolute;
    left: 220px;
    top: 226px;
    width: 760px;
    height: 475px;
    border-radius: 30px;
    overflow: hidden;
    background:
      linear-gradient(160deg, var(--card-light) 0%, var(--card-mid) 32%, var(--card-deep) 62%, var(--card-dark) 100%);
    box-shadow: 0 18px 40px rgba(0, 0, 0, 0.35);
  }
  .ticket__light {
    position: absolute;
    inset: 0;
    background:
      radial-gradient(ellipse 170px 38px at 330px 212px, var(--glow-cyan), transparent 70%),
      radial-gradient(ellipse 260px 150px at 260px 330px, var(--glow-violet), transparent 70%),
      radial-gradient(ellipse 200px 90px at 520px 380px, rgba(120, 90, 255, 0.35), transparent 70%),
      radial-gradient(ellipse 320px 200px at 700px 60px, rgba(140, 110, 255, 0.35), transparent 70%);
  }
  .ticket__band {
    position: absolute;
    left: 300px;
    right: 0;
    top: 208px;
    height: 112px;
    background: var(--band);
  }
  .ticket__title {
    position: absolute;
    left: 300px;
    top: 140px;
    margin: 0;
    font-family: "Roboto", sans-serif;
    font-weight: 100;
    font-size: 52px;
    letter-spacing: 0.5px;
    color: var(--title);
    white-space: nowrap;
  }
  .ticket__verse {
    position: absolute;
    left: 318px;
    top: 220px;
    margin: 0;
    font-family: "Roboto", sans-serif;
    font-weight: 300;
    font-size: 25px;
    line-height: 30px;
    color: var(--verse);
  }
</style>
</head>
<body>
  <main class="canvas">
    <section class="ticket">
      <div class="ticket__light" role="img" aria-label="Abstract swirling light trails in cyan and violet"></div>
      <div class="ticket__band"></div>
      <h1 class="ticket__title">Prom Night 2011</h1>
      <p class="ticket__verse">No sleep till morn<br>On with the dance<br>Let joy be unconfined</p>
    </section>
  </main>
</body>
</html>
```